Personalised Poetry business needs a business card designed

I am a writer that specialises in personalised poetry for people for significant life events.
I want a business card that stands out and portrays class and professionalism but is also welcoming & indicates warmth and honesty.
I'm happy with the logo that was designed for me, I would like to see it in raised print on the business card. I am open to suggestions on colours but think perhaps gold or silver writing for the logo would look good. I would like just the logo and my name and contact details on the front of the card. On the back of the card, I would like a list of the different events I provide poems for I will upload a photo of my current business card for reference. My current logo has a shading behind it that I don't like, I just want the words of the logo without any background colour

Target Market(s)

People wanting to provide a unique gift to someone special in their life

Industry/Entity Type

Writer

Contact Information for Business Card

Logo, my name and contact details on the front and a list of all the events I write poetry for on the back

Font styles to use
Script

Requirements
Must have
• I would like to see the logo, if possible, in a raised type of print on the card so that you can feel the actual words. I would like to have a glossy finish to the card and be able to print it on good quality board
Should not have
• The shading that is currently behind the logo on my current business card

```html
<!DOCTYPE html>
<html lang="en">
<head>
<meta charset="utf-8">
<title>Lines for Always – Business Cards</title>
<link rel="stylesheet" href="https://fonts.googleapis.com/css2?family=Lato:wght@300;400&family=Pinyon+Script&display=swap">
<style>
  :root {
    --backdrop: #1b1b1b;
    --card: #3a3b3d;
    --card-edge: #2f3032;
    --silver: #e6e6e6;
    --silver-soft: #bdbdbd;
    --rule: #8c8c8c;
  }
  * { margin: 0; padding: 0; box-sizing: border-box; }
  html, body {
    width: 1200px; height: 939px; overflow: hidden;
    background: var(--backdrop);
  }
  .canvas {
    position: relative; width: 1200px; height: 939px;
    display: flex; flex-direction: column; align-items: center; justify-content: center;
    gap: 44px;
  }
  .card {
    position: relative; width: 620px; height: 354px;
    border-radius: 22px;
    background: linear-gradient(160deg, #434446 0%, var(--card) 45%, var(--card-edge) 100%);
    box-shadow: 0 14px 30px rgba(0,0,0,.55);
    color: var(--silver);
    font-family: 'Lato', sans-serif;
  }

  /* Back: events */
  .card--events {
    display: flex; flex-direction: column; align-items: center;
    padding-top: 78px; text-align: center;
  }
  .brand-name {
    font-family: 'Lato', sans-serif; font-weight: 300;
    color: var(--silver); letter-spacing: .06em;
  }
  .card--events .brand-name { font-size: 46px; }
  .brand-row { display: flex; align-items: center; gap: 14px; }
  .brand-dot { width: 12px; height: 12px; border-radius: 50%; background: var(--silver); }
  .events-heading {
    margin-top: 62px;
    font-family: 'Pinyon Script', cursive; font-size: 30px; color: var(--silver);
  }
  .events-list {
    list-style: none; margin-top: 10px;
    font-size: 15.5px; line-height: 1.55; letter-spacing: .02em; color: var(--silver);
  }

  /* Front: contact */
  .card--contact { display: flex; align-items: center; }
  .contact-brand {
    width: 330px; display: flex; justify-content: center; padding-top: 20px;
  }
  .card--contact .brand-name { font-size: 30px; }
  .contact-rule {
    width: 1px; height: 150px; background: var(--rule);
  }
  .contact-details { padding-left: 32px; }
  .person-name {
    font-family: 'Pinyon Script', cursive; font-size: 38px; color: var(--silver);
    margin-bottom: 8px;
  }
  .contact-list { list-style: none; font-size: 15.5px; line-height: 1.75; letter-spacing: .02em; }
  .contact-list li { display: flex; align-items: center; gap: 10px; }
  .contact-list svg { width: 12px; height: 12px; fill: var(--silver-soft); flex: none; }
</style>
</head>
<body>
<main class="canvas">

  <section class="card card--events" aria-label="Card back: occasions">
    <div class="brand-row">
      <span class="brand-name">Lines for Always</span>
      <span class="brand-dot" aria-hidden="true"></span>
    </div>
    <h2 class="events-heading">Momentous Life Events Personalised in Poetry</h2>
    <ul class="events-list">
      <li>Weddings &amp; Anniversaries • Birthdays &amp; Christmas • Valentines Day</li>
      <li>Retirements, Business &amp; Corporate • Funerals &amp; Eulogies</li>
    </ul>
  </section>

  <section class="card card--contact" aria-label="Card front: contact">
    <div class="contact-brand">
      <div class="brand-row">
        <span class="brand-name">Lines for Always</span>
        <span class="brand-dot" aria-hidden="true"></span>
      </div>
    </div>
    <div class="contact-rule" aria-hidden="true"></div>
    <div class="contact-details">
      <p class="person-name">Martin Ellery</p>
      <ul class="contact-list">
        <li>
          <svg viewBox="0 0 24 24" aria-hidden="true"><path d="M6.6 10.8a15.1 15.1 0 0 0 6.6 6.6l2.2-2.2a1 1 0 0 1 1-.25 11.4 11.4 0 0 0 3.6.57 1 1 0 0 1 1 1V20a1 1 0 0 1-1 1A17 17 0 0 1 3 4a1 1 0 0 1 1-1h3.5a1 1 0 0 1 1 1c0 1.25.2 2.45.57 3.57a1 1 0 0 1-.25 1z"/></svg>
          0400 123 456
        </li>
        <li>
          <svg viewBox="0 0 24 24" aria-hidden="true"><path d="M2 5h20v14H2z M2 5l10 8 10-8" fill="none" stroke="#bdbdbd" stroke-width="2.4"/></svg>
          martin@linesforalways.com
        </li>
        <li>
          <svg viewBox="0 0 24 24" aria-hidden="true"><circle cx="12" cy="12" r="10"/><path d="M2 12h20M12 2c3 3 3 17 0 20M12 2c-3 3-3 17 0 20" fill="none" stroke="#3a3b3d" stroke-width="1.6"/></svg>
          linesforalways.com
        </li>
      </ul>
    </div>
  </section>

</main>
</body>
</html>
```